Real Estate Marketing Postcards need a fresh look, Front & Back

I have a current postcard design (attached) that lacks design quality and too much use of color. I do like the basic color scheme, but I'm open to anything that cleans up the look and incorporates space for the existing text. I'm not opposed to a design with a white background, more white space. The design should be full bleed according to the attached specs. I would like this to be sent over in an Adobe format, something like InDesign.

The company logo will remain the same colors and appearance. The headshot will likely be updated in the coming weeks.

I am attaching a sample of a recent card plus a template from the printer showing the back of the card and location of the address and postage section that must remain blank. I am also including the logo and another logo designed for use with a white (or non blue) background.

(feel free to swap in stock photos of whatever house you want, but the front of the card should incorporate at least one photo of a house.)

Target Market(s)

Home owners.

Industry/Entity Type

Real Estate

Font styles to use
Sans Serif

Colors

Designer to choose colors to be used in the design.

Requirements
Must have
• Company logo, the headshot, the contact info on the back, a photo or photos of a house along with the text "Just Sold" or "Sold" featured on the front of the card.

```html
<!DOCTYPE html>
<html lang="en">
<head>
<meta charset="utf-8">
<title>Willow Run Real Estate – Postcard Front &amp; Back</title>
<link rel="stylesheet" href="https://fonts.googleapis.com/css2?family=Lato:wght@400;700&family=Roboto+Condensed:wght@300;700&display=swap">
<style>
  :root{
    --navy:#0d4a86;
    --blue:#1463ad;
    --lime:#b9d32c;
    --white:#ffffff;
    --bg:#e9e9e9;
    --ink:#111111;
    --sky-top:#3f8fd8;
    --sky-low:#cfe4f5;
    --lawn:#5f9a34;
  }
  *{box-sizing:border-box;margin:0;padding:0}
  html,body{width:1200px;height:1200px;overflow:hidden;background:var(--bg)}
  .canvas{position:relative;width:1200px;height:1200px}
  .card{position:absolute;left:212px;width:776px;height:546px;overflow:hidden;background:var(--white);box-shadow:0 2px 10px rgba(0,0,0,.18)}
  .card--front{top:26px}
  .card--back{top:628px}

  /* FRONT */
  .house-photo{position:absolute;left:0;top:0;width:776px;height:398px;
    background:linear-gradient(180deg,var(--sky-top) 0%,var(--sky-low) 48%,#b9aa98 62%,var(--lawn) 82%,#4d8229 100%)}
  .front-band{position:absolute;left:0;top:398px;width:776px;height:148px}
  .brand{position:absolute;font-family:'Lato',sans-serif;font-weight:700;color:var(--blue);line-height:1}
  .brand--front{left:28px;top:478px;font-size:34px;letter-spacing:-.5px}
  .brand--front small{display:block;font-size:13px;letter-spacing:3px;margin-top:6px;text-align:right}
  .headline{position:absolute;right:56px;top:406px;text-align:right;color:var(--white);font-family:'Roboto Condensed',sans-serif;white-space:nowrap}
  .headline__lead{font-weight:300;font-size:42px;line-height:1.1;letter-spacing:-.5px}
  .headline__lead strong{font-weight:700;color:var(--lime)}
  .headline__lead span{font-size:27px}
  .headline__title{font-weight:700;font-size:44px;line-height:1.05;letter-spacing:-.3px}
  .headline__tag{font-weight:700;font-size:19px;margin-top:12px}

  /* BACK */
  .back-shape{position:absolute;left:0;top:0;width:776px;height:546px}
  .pitch{position:absolute;left:29px;top:24px;width:350px;color:var(--white);font-family:'Roboto Condensed',sans-serif;font-weight:700}
  .pitch__title{font-size:60px;line-height:1;letter-spacing:-.5px}
  .pitch__sub{font-size:28px;line-height:38px;margin-top:2px;letter-spacing:-.2px}
  .headshot{position:absolute;left:406px;top:30px;width:125px;height:120px;background:linear-gradient(180deg,#bdbfc4,#8f9297)}
  .copy{position:absolute;left:29px;top:169px;width:478px;color:var(--white);font-family:'Lato',sans-serif;font-size:10.4px;line-height:13.6px}
  .copy p{margin-bottom:13.6px}
  .copy p.narrow{width:442px}
  .copy p.gap{margin-bottom:21.6px}
  .copy p.wide-gap{margin-bottom:16px}
  .contact{position:absolute;left:29px;top:406px;color:var(--white);font-family:'Lato',sans-serif;font-size:15px;line-height:18.4px}
  .contact__name{font-weight:700;font-size:16px}
  .contact__row{display:flex;align-items:center;gap:5px}
  .contact__row svg{width:12px;height:12px;flex:none}
  .brand--back{left:610px;top:52px;font-size:24px;letter-spacing:-.3px}
  .brand--back small{display:block;font-size:10px;letter-spacing:2.5px;margin-top:4px;text-align:right}
  .stamp{position:absolute;left:683px;top:280px;width:60px;height:60px;border:2px solid var(--ink)}
  .address-line{position:absolute;left:561px;width:184px;height:2px;background:var(--ink)}
</style>
</head>
<body>
<main class="canvas">

  <section class="card card--front" aria-label="Postcard front">
    <div class="house-photo" role="img" aria-label="Photo of a large two-storey suburban house with manicured lawn and flowering shrubs under a blue sky"></div>
    <svg class="front-band" viewBox="0 0 776 148" aria-hidden="true">
      <defs>
        <linearGradient id="bandBlue" x1="0" x2="1" y1="0" y2="0">
          <stop offset="0" stop-color="#0e4f8f"/>
          <stop offset="1" stop-color="#1a6db8"/>
        </linearGradient>
      </defs>
      <polygon points="244,0 776,0 776,148 312,148" fill="url(#bandBlue)"/>
      <polygon points="236,12 248,12 310,148 298,148" fill="var(--lime)"/>
    </svg>
    <div class="brand brand--front">willow run<small>REAL ESTATE</small></div>
    <div class="headline">
      <div class="headline__lead">Another home Just <strong>SOLD</strong> <span>by</span></div>
      <div class="headline__title">THE OAKMERE REALTOR</div>
      <div class="headline__tag">You KNOW it won’t last long!</div>
    </div>
  </section>

  <section class="card card--back" aria-label="Postcard back">
    <svg class="back-shape" viewBox="0 0 776 546" aria-hidden="true">
      <polygon points="0,0 588,0 468,546 0,546" fill="var(--navy)"/>
      <polygon points="580,102 592,102 486,546 466,546" fill="var(--lime)"/>
    </svg>

    <div class="pitch">
      <div class="pitch__title">SELLING???</div>
      <div class="pitch__sub">Choosing the right agent is critical to your success.</div>
    </div>
    <div class="headshot" role="img" aria-label="Agent headshot portrait"></div>

    <div class="copy">
      <p>Your home is your biggest asset. You owe it to yourself to have every advantage by choosing the local agent with the expertise to position your Oakmere home and get it sold fast and for top dollar.</p>
      <p class="gap">There is no other agent who knows the Oakmere market better. Contact me today to get your home SOLD.</p>
      <p class="narrow">Your home is your biggest asset. You owe it to yourself to have every advantage by choosing the local agent with the expertise to position your Oakmere home and get it sold fast and for top dollar.</p>
      <p class="narrow wide-gap">There is no other agent who knows the Oakmere market better. Contact me today to get your home SOLD.</p>
      <p class="narrow">Contact me today to discuss your home’s value and what steps I will take to assure your success.</p>
    </div>

    <div class="contact">
      <div class="contact__name">Dario Belmonte</div>
      <div>“The Oakmere Realtor”</div>
      <div>Principal Broker, REALTOR</div>
      <div>Willow Run Real Estate</div>
      <div class="contact__row">
        <svg viewBox="0 0 12 12" aria-hidden="true"><circle cx="6" cy="6" r="5.3" fill="none" stroke="var(--lime)" stroke-width="1.2"/><path d="M4 3.3l1 .1.5 1.3-.6.5c.3.7.8 1.2 1.5 1.5l.5-.6 1.3.5.1 1c-2.3.4-4.6-1.9-4.3-4.3z" fill="var(--lime)"/></svg>
        <span>(555) 210-4040</span>
        <svg viewBox="0 0 12 12" aria-hidden="true" style="margin-left:6px"><circle cx="6" cy="6" r="5.3" fill="none" stroke="var(--lime)" stroke-width="1.2"/><path d="M4 3.3l1 .1.5 1.3-.6.5c.3.7.8 1.2 1.5 1.5l.5-.6 1.3.5.1 1c-2.3.4-4.6-1.9-4.3-4.3z" fill="var(--lime)"/></svg>
        <span>(555) 807-1290 Cell</span>
      </div>
      <div class="contact__row">
        <svg viewBox="0 0 12 12" aria-hidden="true"><circle cx="6" cy="6" r="5.2" fill="none" stroke="var(--lime)" stroke-width="1.1"/><ellipse cx="6" cy="6" rx="2.3" ry="5.2" fill="none" stroke="var(--lime)" stroke-width="1"/><path d="M1 6h10M1.8 3.5h8.4M1.8 8.5h8.4" stroke="var(--lime)" stroke-width=".9"/></svg>
        <span>www.OakmereHomes.com</span>
      </div>
    </div>

    <div class="brand brand--back">willow run<small>REAL ESTATE</small></div>
    <div class="stamp" aria-label="Postage area"></div>
    <div class="address-line" style="top:389px"></div>
    <div class="address-line" style="top:422px"></div>
    <div class="address-line" style="top:455px"></div>
  </section>

</main>
</body>
</html>
```